Help us share the power of history

We need 5 flyers (they can be similar in design, just small content changes in the front) and 1 large poster.

Paper Lanterns? is a movement that aims to change the history market so that everyone gets what they need to be a changemaker of society. We've been selected as one of the most promising startups in Massachusetts and we will have a booth at FERNFest's Pitch Day.

We are trying to attract the attention of people walking buy to invest in our pledgebarn campaign.

Target Market(s)

500-1,000 social entrepreneurs who are going to be walking around a large convention hall - so everything in terms of colors and design needs to be attractive

Industry/Entity Type

Non Profit

Font styles to use
Other font styles liked:
• Phoenix American

Colors

Designer to choose colors to be used in the design.

Requirements
Must have
• Font type: Phoenix American
• Modern
• Easy to read
• Eye-catching
• Please see attached document for more information.

```html
<!DOCTYPE html>
<html lang="en">
<head>
<meta charset="utf-8">
<title>paper lanterns? – flyer</title>
<link href="https://fonts.googleapis.com/css2?family=Pathway+Gothic+One&family=Josefin+Sans:wght@400&display=swap" rel="stylesheet">
<style>
  :root {
    --page-bg: #efe6de;
    --ink-black: #000000;
    --brand-purple: #532d84;
    --accent-gold: #e3a52a;
    --url-yellow: #f4bc12;
    --text-white: #ffffff;
    --list-text: #f1ecf6;
  }
  html, body {
    margin: 0;
    padding: 0;
    width: 1200px;
    height: 1200px;
    overflow: hidden;
    background: var(--page-bg);
  }
  .flyer {
    position: absolute;
    left: 320px;
    top: 40px;
    width: 560px;
    height: 1120px;
    background: var(--brand-purple);
    overflow: hidden;
    box-shadow: 0 14px 24px rgba(0,0,0,0.25);
  }
  .flyer-art {
    position: absolute;
    inset: 0;
    width: 560px;
    height: 1120px;
  }
  .headline {
    position: absolute;
    left: 0;
    right: 0;
    top: 130px;
    margin: 0;
    text-align: center;
    font-family: "Pathway Gothic One", sans-serif;
    font-weight: 400;
    font-size: 82px;
    line-height: 1;
    color: var(--text-white);
  }
  .mission {
    position: absolute;
    left: 30px;
    right: 30px;
    top: 244px;
    margin: 0;
    text-align: center;
    font-family: "Pathway Gothic One", sans-serif;
    font-size: 35px;
    line-height: 40px;
    color: var(--text-white);
  }
  .services-title {
    position: absolute;
    left: 51px;
    top: 708px;
    margin: 0;
    font-family: "Pathway Gothic One", sans-serif;
    font-weight: 400;
    font-size: 52px;
    line-height: 1;
    color: var(--text-white);
  }
  .services {
    position: absolute;
    left: 0;
    top: 0;
    margin: 0;
    padding: 0;
    list-style: none;
  }
  .service {
    position: absolute;
    left: 49px;
    height: 42px;
    display: flex;
    align-items: center;
    white-space: nowrap;
    font-family: "Josefin Sans", sans-serif;
    font-size: 19px;
    letter-spacing: 2.6px;
    color: var(--list-text);
  }
  .service-icon {
    width: 42px;
    height: 42px;
    margin-right: 23px;
    flex: none;
  }
  .site-url {
    position: absolute;
    left: 0;
    right: 0;
    top: 1028px;
    margin: 0;
    text-align: center;
    font-family: "Pathway Gothic One", sans-serif;
    font-size: 48px;
    line-height: 1;
    letter-spacing: 6px;
    color: var(--url-yellow);
  }
</style>
</head>
<body>
  <main class="flyer">
    <svg class="flyer-art" viewBox="0 0 560 1120" xmlns="http://www.w3.org/2000/svg">
      <defs>
        <linearGradient id="heroFade" x1="0" y1="0" x2="0" y2="1">
          <stop offset="0" stop-color="#000000"/>
          <stop offset="0.28" stop-color="#000000"/>
          <stop offset="0.45" stop-color="#4a4a4c"/>
          <stop offset="0.55" stop-color="#5a534b"/>
          <stop offset="0.75" stop-color="#4b4540"/>
          <stop offset="1" stop-color="#2f2d2c"/>
        </linearGradient>
      </defs>
      <rect class="hero-photo" x="0" y="0" width="560" height="1000" fill="url(#heroFade)"
            role="img" aria-label="Photo of two children wrapped in a flag, walking a winding country road with wind turbines behind"/>
      <polygon class="brush-top" fill="var(--brand-purple)"
        points="30,0 560,0 560,172 540,160 548,168 510,146 520,155 470,125 482,136 430,104 440,113 390,82 398,90 340,56 352,66 300,40 310,48 250,24 262,33 200,14 214,22 150,8 165,14 100,4 115,9 60,2"/>
      <polygon class="brush-bottom" fill="var(--brand-purple)"
        points="0,626 20,636 10,628 60,652 48,644 110,670 98,662 160,692 150,684 210,712 198,704 270,736 258,728 330,756 318,748 390,772 380,764 450,784 440,778 510,790 500,784 560,796 560,1120 0,1120"/>
    </svg>

    <h1 class="headline">paper lanterns?</h1>
    <p class="mission">We are a systems change initiative to<br>strengthen democracy by enabling everyone<br>to have access to the power of history</p>

    <h2 class="services-title">What we do:</h2>
    <ul class="services">
      <li class="service" style="top:800px">
        <svg class="service-icon" viewBox="0 0 42 42"><g fill="none" stroke="var(--accent-gold)" stroke-width="1.3"><circle cx="21" cy="21" r="20"/><rect x="13" y="16" width="16" height="11" rx="1"/><path d="M18 16v-2h6v2M13 21h16"/></g></svg>
        Frame Purpose and Power of History
      </li>
      <li class="service" style="top:850px">
        <svg class="service-icon" viewBox="0 0 42 42"><g fill="none" stroke="var(--accent-gold)" stroke-width="1.3"><circle cx="21" cy="21" r="20"/><circle cx="21" cy="21" r="8"/><path d="M21 16v10M19 18h4"/></g></svg>
        Enable Innovation
      </li>
      <li class="service" style="top:898px">
        <svg class="service-icon" viewBox="0 0 42 42"><g fill="none" stroke="var(--accent-gold)" stroke-width="1.3"><circle cx="21" cy="21" r="20"/><path d="M14 28l2-6 10-10 4 4-10 10z M24 14l4 4"/></g></svg>
        Spread What Works
      </li>
      <li class="service" style="top:947px">
        <svg class="service-icon" viewBox="0 0 42 42"><g fill="none" stroke="var(--accent-gold)" stroke-width="1.3"><circle cx="21" cy="21" r="20"/><path d="M13 14h16v10H19l-4 4v-4h-2z"/><path d="M17 19h8"/></g></svg>
        Change Conversation
      </li>
    </ul>

    <p class="site-url">www.paper-lanterns.org</p>
  </main>
</body>
</html>
```